Business Card Design Project

We need a business card for our business called Our Harbour Lender. (www.ourharbourlender.com.au)

There are 3 of us in the business, the design we choose will stay the same for all 3 of us, but will need names changed and mobile numbers added. I will provide details in an attachment.

We are a professional services directory for mortgage brokers. I will attach an idea that I had, but happy for you to be free in your designs. We would like the colour scheme to remain within our company colours - blue, white, grey and orange.

Thanks so much for helping us with this project. If you need anymore information, please don't hesitate to ask.

Industry/Entity Type

Business

Requirements
Must have
• Our Harbour Lender Logo
Colour blue and orange to match closely with our logo samples if possible.
The most important card is the card for Tilda Brennan

```html
<!DOCTYPE html>
<html lang="en">
<head>
<meta charset="utf-8">
<title>Our Harbour Lender — Business Card</title>
<link rel="stylesheet" href="https://fonts.googleapis.com/css2?family=Arimo:wght@400;700&display=swap">
<style>
  :root {
    --page-bg: #ececec;
    --card-blue: #1b96d6;
    --card-blue-light: #2eaee6;
    --card-white: #ffffff;
    --accent-grey: #a3a7ab;
    --divider: rgba(255, 255, 255, 0.55);
  }
  * { box-sizing: border-box; margin: 0; padding: 0; }
  html, body {
    width: 1200px;
    height: 1200px;
    overflow: hidden;
    background: var(--page-bg);
    font-family: "Arimo", Arial, sans-serif;
  }
  .canvas {
    position: relative;
    width: 1200px;
    height: 1200px;
  }
  .card {
    position: absolute;
    left: 240px;
    width: 720px;
    height: 415px;
    border-radius: 30px;
    background: radial-gradient(ellipse at 50% 50%, var(--card-blue-light) 0%, var(--card-blue) 75%);
    color: var(--card-white);
    overflow: hidden;
  }
  .card--front { top: 130px; }
  .card--back { top: 640px; }

  /* Front */
  .front-brand {
    position: absolute;
    left: 0; right: 0; top: 160px;
    display: flex;
    align-items: center;
    justify-content: center;
    gap: 18px;
  }
  .brand-dot {
    width: 58px; height: 58px;
    border-radius: 50%;
    border: 7px solid var(--card-white);
  }
  .brand-name {
    font-size: 64px;
    font-weight: 400;
    letter-spacing: -1px;
    color: var(--card-white);
    line-height: 1;
  }

  /* Back */
  .back-left {
    position: absolute;
    left: 40px; top: 230px;
    width: 300px;
    text-align: center;
  }
  .back-brand {
    display: flex;
    align-items: center;
    justify-content: center;
    gap: 10px;
    margin-bottom: 16px;
  }
  .back-brand .brand-dot { width: 28px; height: 28px; border-width: 4px; }
  .back-brand .brand-name { font-size: 30px; letter-spacing: -0.5px; }
  .entity-note {
    font-size: 13px;
    font-weight: 700;
    line-height: 1.25;
    text-transform: uppercase;
  }
  .entity-note .entity-name { color: var(--accent-grey); display: block; font-size: 14px; }

  .back-divider {
    position: absolute;
    left: 382px; top: 110px;
    width: 2px; height: 195px;
    background: var(--divider);
  }
  .back-right {
    position: absolute;
    right: 44px; top: 56px;
    text-align: right;
    font-weight: 700;
    font-size: 14px;
    line-height: 1.25;
  }
  .person-name { color: var(--accent-grey); font-size: 28px; line-height: 1; }
  .person-role { font-size: 14px; margin-bottom: 22px; }
  .company-abn { margin-bottom: 22px; }
  .contact-list { list-style: none; margin-bottom: 22px; }
  .contact-label { color: var(--accent-grey); margin-right: 4px; }
</style>
</head>
<body>
<main class="canvas">
  <section class="card card--front" aria-label="Card front">
    <div class="front-brand">
      <span class="brand-dot" aria-hidden="true"></span>
      <span class="brand-name">Our Harbour Lender</span>
    </div>
  </section>

  <section class="card card--back" aria-label="Card back">
    <div class="back-left">
      <div class="back-brand">
        <span class="brand-dot" aria-hidden="true"></span>
        <span class="brand-name">Our Harbour Lender</span>
      </div>
      <p class="entity-note">
        <span class="entity-name">Our Harbour Lender</span>
        is a Tidewater Finance Group<br>Pty Ltd Project
      </p>
    </div>

    <div class="back-divider" aria-hidden="true"></div>

    <div class="back-right">
      <p class="person-name">Tilda Brennan</p>
      <p class="person-role">CEO/Founder</p>
      <p class="company-abn">ABN 41 602 318 775</p>
      <ul class="contact-list">
        <li><span class="contact-label">P</span>1300 HARBOUR</li>
        <li><span class="contact-label">M</span>0438 215 907</li>
        <li><span class="contact-label">F</span>02 9164 3382</li>
      </ul>
      <p class="contact-email">tilda@ourharbourlender.com</p>
      <p class="contact-web">www.ourharbourlender.com.au</p>
    </div>
  </section>
</main>
</body>
</html>
```